Darrow Kettle Lawyers needs a web design

We need a web design for our conveyancing and commercial law firm based in Sydney Australia. We want to depersonalise the current website: http://www.darrowkettle-example.com/ and give it a classic modern feel to it. It should be a simple design (possibly one page) and communicate trust, professionalism and experience.

Content should include:

Darrow Kettle is a boutique Sydney based legal practice specialising in business and property law.

We pride ourselves on our proactive, receptive and dynamic approach to client service. Our business survives on referrals from satisfied clients and professionals who respect the way we do business.

Practice areas

Business law

We act on the sale and purchase of businesses. We assist clients with structuring their businesses, drafting shareholder agreements and buy-sell arrangements. We have acted on a multitude of other commercial matters including franchising, distribution, marketing and business services (with a particular focus in the advertising sector).

Property law

We act for developers, commercial property investors, landlords and tenants. We also handle residential conveyancing and deal with strata and company title matters.

Private Client

We draft wills and codicils on behalf of clients and can also assist with applications for probate should the need arise.

Contact Us

Darrow Kettle
Level 14, Marlow Spire
7 Brennock Plaza
Sydney, NSW 2000

t: +61 (0)2 9471 6023
f: +61 (0)2 8265 4790
e: enquiries@darrowkettle-example.com

Target Market(s)

Individuals and business who need legal advice in the area of property and commercial law

Industry/Entity Type

Legal

Number of Pages Required

1 page

Font styles to use
Sans Serif

Requirements
Must have
• Clear and concise content.
Nice to have
• Some images to break up the content.
Should not have
• Any offensive images tones or connotations.

```html
<!DOCTYPE html>
<html lang="en">
<head>
<meta charset="utf-8">
<title>Darrow Kettle Lawyers</title>
<link rel="stylesheet" href="https://fonts.googleapis.com/css2?family=Open+Sans:ital,wght@0,400;0,600;1,400&display=swap">
<style>
:root{
  --blue:#1b4f9c;
  --blue-dark:#173f7d;
  --ink:#333;
  --text:#444;
  --muted:#666;
  --rule:#e6e6e6;
  --footer:#353535;
  --footer-low:#2a2a2a;
  --field:#555;
  --foot-text:#ddd;
}
*{box-sizing:border-box;margin:0;padding:0}
html,body{width:918px;height:1200px;overflow:hidden;background:#fff}
body{position:relative;font-family:"Open Sans",Arial,sans-serif;color:var(--text)}
.abs{position:absolute}

.site-header{left:0;top:0;width:918px;height:61px;background:#fff;box-shadow:0 1px 3px rgba(0,0,0,.15);z-index:2}
.brand{left:122px;top:11px;font-size:24px;color:#555;letter-spacing:-.3px;line-height:1}
.brand-sub{left:242px;top:40px;font-size:11px;color:var(--blue);line-height:1}
.nav{top:28px;font-size:8.5px;font-weight:600;color:#222;line-height:1}
.nav.active{color:var(--blue)}

.hero{left:0;top:61px;width:918px;height:373px;background:linear-gradient(180deg,#7b9ac7 0%,#c9a77a 38%,#e09a3c 55%,#8a5a22 70%,#c68633 85%,#5e3c18 100%)}
.hero-card{left:542px;top:175px;width:253px;height:137px;background:var(--blue);color:#fff;text-align:right;padding:22px 22px 0 22px}
.hero-card h1{font-weight:400;font-size:21px;line-height:1}
.hero-card p{font-style:italic;font-size:11.5px;line-height:18px;margin-top:18px}
.slide-prev{left:0;top:221px;width:38px;height:56px;background:rgba(60,60,60,.45)}
.slide-next{left:886px;top:221px;width:32px;height:56px}

.welcome-title{left:124px;top:470px;font-size:18px;font-weight:400;color:var(--ink)}
.welcome-text{left:122px;top:505px;width:350px;font-size:8.4px;line-height:15.6px;color:var(--text)}
.welcome-text em{color:var(--blue);font-weight:600}
.frame{border:1px solid var(--rule);padding:3px;background:#fff}
.photo{width:100%;height:100%}
.divider{left:122px;top:644px;width:673px;height:1px;background:var(--rule)}
.section-title{left:122px;top:658px;font-size:18px;font-weight:400;color:var(--ink)}

.card-title{font-size:12px;font-weight:600;color:var(--blue-dark);line-height:1}
.card-text{font-size:7.7px;line-height:15px;color:var(--text);width:215px}
.btn{display:flex;align-items:center;justify-content:center;width:66px;height:26px;background:var(--blue);color:#fff;font-size:7.7px;border-radius:2px;border:1px solid #0f3a78}

.footer{left:0;top:990px;width:918px;height:172px;background:var(--footer)}
.footer-base{left:0;top:1162px;width:918px;height:38px;background:var(--footer-low);color:#ccc;font-size:7.7px;display:flex;align-items:center;justify-content:center}
.foot-title{font-size:11.5px;color:#fff;line-height:1}
.field{background:var(--field);border:1px solid #4a4a4a;color:#bbb;font-size:7px;font-style:italic;padding:4px 7px}
.submit{left:122px;top:1118px;width:57px;height:19px;background:var(--blue);color:#fff;font-size:7px;font-weight:600;display:flex;align-items:center;justify-content:center}
.vrule{width:1px;background:#444}
.contact-line{left:506px;font-size:7.7px;color:var(--foot-text);line-height:1;display:flex;align-items:center;gap:6px}
.contact-line svg{width:7px;height:7px;fill:#ccc;flex:none}
.service{left:744px;font-size:7.7px;color:var(--foot-text);line-height:1}
</style>
</head>
<body>

<header class="abs site-header">
  <div class="abs brand">Darrow Kettle</div>
  <div class="abs brand-sub">Lawyers</div>
  <div class="abs nav active" style="left:585px">HOME</div>
  <div class="abs nav" style="left:642px">PRACTICE AREAS</div>
  <div class="abs nav" style="left:742px">CONTACT US</div>
</header>

<section class="abs hero" role="img" aria-label="Sydney harbour skyline at sunset reflected in the water"></section>
<div class="abs slide-prev">
  <svg width="38" height="56" viewBox="0 0 38 56"><path d="M24 16 L12 28 L24 40" fill="none" stroke="#fff" stroke-width="1.5"/></svg>
</div>
<div class="abs slide-next">
  <svg width="32" height="56" viewBox="0 0 32 56"><path d="M8 16 L20 28 L8 40" fill="none" stroke="#fff" stroke-width="1.5"/></svg>
</div>
<div class="abs hero-card">
  <h1>Darrow Kettle</h1>
  <p>Darrow Kettle is a boutique law firm based in Sydney specialising in business and property law.</p>
</div>

<h2 class="abs welcome-title">Welcome to Darrow Kettle</h2>
<p class="abs welcome-text">Darrow Kettle is a boutique Sydney based legal practice specialising in business and property law. We pride ourselves on our proactive, receptive and dynamic approach to client service. Our business survives on referrals from satisfied clients and professionals who respect the way we do business.<em>We look forward to hearing from you.</em></p>
<div class="abs frame" style="left:565px;top:460px;width:229px;height:153px">
  <div class="photo" role="img" aria-label="Hand signing a document beside a statue of justice" style="background:linear-gradient(135deg,#3a3430 0%,#6d6560 45%,#c9c9cc 75%,#e6e6ea 100%)"></div>
</div>

<div class="abs divider"></div>
<h2 class="abs section-title">Practice Areas</h2>

<div class="abs frame" style="left:122px;top:694px;width:212px;height:135px">
  <div class="photo" role="img" aria-label="Business team gathered around a laptop" style="background:linear-gradient(135deg,#2a2a2e 0%,#8a7b70 45%,#d8d2cc 70%,#3c3c40 100%)"></div>
</div>
<div class="abs frame" style="left:354px;top:694px;width:212px;height:135px">
  <div class="photo" role="img" aria-label="Glass office tower seen from below" style="background:linear-gradient(135deg,#9fb8d4 0%,#3f6b9c 40%,#c8d6e4 65%,#284a72 100%)"></div>
</div>
<div class="abs frame" style="left:583px;top:694px;width:211px;height:135px">
  <div class="photo" role="img" aria-label="Client meeting across a desk in an office" style="background:linear-gradient(135deg,#3a3330 0%,#8c8c90 45%,#6f96c4 65%,#2a2626 100%)"></div>
</div>

<h3 class="abs card-title" style="left:123px;top:844px">Business law</h3>
<p class="abs card-text" style="left:122px;top:864px">We act on the sale and purchase of businesses. We assist clients with structuring their businesses, drafting shareholder agreements and buy-sell arrangements.</p>
<div class="abs btn" style="left:122px;top:918px">READ MORE</div>

<h3 class="abs card-title" style="left:354px;top:844px">Property law</h3>
<p class="abs card-text" style="left:353px;top:864px">We act for developers, commercial property investors, landlords and tenants. We also handle residential conveyancing and deal with strata and company</p>
<div class="abs btn" style="left:353px;top:918px">READ MORE</div>

<h3 class="abs card-title" style="left:583px;top:844px">Private Client</h3>
<p class="abs card-text" style="left:582px;top:864px;width:212px">We draft wills and codicils on behalf of clients and can also assist with applications for probate should the need arise. We can help with setting up family trusts, unit trusts, powers of attorney and business succession issues.</p>
<div class="abs btn" style="left:582px;top:946px">READ MORE</div>

<footer class="abs footer"></footer>
<div class="abs foot-title" style="left:122px;top:1011px">Contact Form</div>
<div class="abs field" style="left:122px;top:1039px;width:146px;height:21px">Name</div>
<div class="abs field" style="left:122px;top:1064px;width:146px;height:22px">Email:</div>
<div class="abs field" style="left:122px;top:1090px;width:146px;height:21px">Phone</div>
<div class="abs field" style="left:273px;top:1039px;width:146px;height:72px">Message:</div>
<div class="abs submit">SUBMIT</div>

<div class="abs vrule" style="left:465px;top:1025px;height:100px"></div>
<div class="abs vrule" style="left:699px;top:1025px;height:100px"></div>

<div class="abs foot-title" style="left:506px;top:1011px">Contact Us</div>
<div class="abs contact-line" style="top:1041px"><svg viewBox="0 0 10 10"><path d="M5 0a3.5 3.5 0 0 0-3.5 3.5C1.5 6 5 10 5 10s3.5-4 3.5-6.5A3.5 3.5 0 0 0 5 0zm0 5a1.4 1.4 0 1 1 0-2.8A1.4 1.4 0 0 1 5 5z"/></svg>Darrow Kettle, Level 14, Marlow Spire</div>
<div class="abs contact-line" style="top:1056px;left:519px">7 Brennock Plaza Sydney, NSW 2000</div>
<div class="abs contact-line" style="top:1075px"><svg viewBox="0 0 10 10"><path d="M2 0l2 2.5-1 1.3c.6 1.3 1.6 2.3 2.9 2.9l1.3-1L10 7.8 8.6 10C4 9.6.4 6 0 1.4z"/></svg>t: +61 (0)2 9471 6023</div>
<div class="abs contact-line" style="top:1090px"><svg viewBox="0 0 10 10"><path d="M2 0h5v3H2zM0 3.5h10V9H8v1H2V9H0zm2.5 3.5v2h5V7z"/></svg>f: +61 (0)2 8265 4790</div>
<div class="abs contact-line" style="top:1105px"><svg viewBox="0 0 10 10"><path d="M0 2h10v6H0zm1 .8L5 5.5l4-2.7"/></svg>e: enquiries@darrowkettle-example.com</div>

<div class="abs foot-title" style="left:742px;top:1011px">Services</div>
<div class="abs service" style="top:1041px">Business Law</div>
<div class="abs service" style="top:1056px">Property Law</div>
<div class="abs service" style="top:1071px">Private Client</div>

<div class="abs footer-base">© 2015 darrow kettle. All copyrights are reserved.</div>

</body>
</html>
```